SkyVane Weather Newsletter Design

Attached is a copy of a weekly newsletter that contains commentary and maps used to discuss all relevant information about weather forecasts. I need to create a newsletter (template) where content can be systematically input into a unique SkyVane format. The object is to deliver a unique design that captures the essence of the firm, the brand, and can be easily used by the team developing the maps and narrative. All logo and related background information may be obtained on the Skyvane website.
Updates

I am just checking to see if there is any interest anywhere in this type of project. This project requires a combination of layout skills and border design work. Any feedback?Dale Added Friday, May 6, 2016

Target Market(s)

Institutional users of weather data, airports, military, governmental agencies, oil companies, news broadcasters, etc.

Requirements
Must have
• Unique design and format. Flexibility to place a number of maps in and around narrative used in the weekly newsletter.
Nice to have
• We have no preference on font. If additional photos of maps are required, please inquire.
Should not have
• Have one solid background color that will use a lot of toner if needed to print out. It can often clash with the multi color nature of the maps.

```html
<!DOCTYPE html>
<html lang="en">
<head>
<meta charset="utf-8">
<title>SkyVane Weather Newsletter</title>
<link rel="stylesheet" href="https://fonts.googleapis.com/css2?family=Nunito+Sans:wght@400;600;700;800&display=swap">
<style>
  :root {
    --brand-blue: #1f6fb5;
    --accent-blue: #1b8fd2;
    --frame-blue: #2f7fc1;
    --ink: #1c1c1c;
    --muted: #6d6f73;
    --rule: #222;
    --paper: #ffffff;
    --map-grey: #e4e7eb;
    --map-soft: #f1f3f4;
    --map-green: #d3e6cf;
  }
  * { box-sizing: border-box; margin: 0; padding: 0; }
  html, body { width: 929px; height: 1200px; overflow: hidden; background: var(--paper); }
  body {
    position: relative;
    font-family: "Nunito Sans", Arial, sans-serif;
    color: var(--ink);
    font-size: 15.5px;
    line-height: 19.5px;
  }
  .edge-band {
    position: absolute; left: 0; top: 0; width: 22px; height: 1200px;
    background: var(--brand-blue);
  }
  .sidebar { position: absolute; left: 56px; top: 180px; width: 262px; }
  .brand { display: flex; align-items: center; gap: 8px; height: 52px; }
  .brand-mark { width: 14px; height: 14px; background: var(--brand-blue); }
  .brand-name {
    font-size: 46px; line-height: 52px; font-weight: 800; color: var(--brand-blue);
    letter-spacing: -0.5px;
  }
  .brand-tagline {
    margin-top: 2px; font-size: 8.5px; letter-spacing: 1.8px; color: var(--muted);
    text-transform: uppercase; text-align: right; width: 262px;
  }
  .author { margin-top: 36px; font-size: 15.5px; line-height: 19.5px; }
  .sidebar-rule { margin: 8px 0 10px; width: 213px; border: 0; border-top: 1.5px solid var(--rule); }
  .issue-date { margin-bottom: 20px; }
  .sidebar p { margin-bottom: 10px; }
  .main p { margin-bottom: 10px; }
  .highlight { color: var(--accent-blue); }
  .main { position: absolute; left: 335px; top: 10px; width: 553px; }
  .map-frame {
    border: 3px solid var(--frame-blue);
    width: 553px;
  }
  .map-frame.reports {
    height: 396px; margin-top: 12px;
    background: linear-gradient(180deg, var(--map-grey) 0%, var(--map-soft) 100%);
  }
  .map-frame.outlook {
    height: 384px; margin-top: 14px;
    background: linear-gradient(180deg, var(--map-soft) 0%, var(--map-green) 100%);
  }
  .map-caption { font-weight: 700; margin: 14px 0 10px; }
  .footer-rule {
    position: absolute; left: 56px; top: 1128px; width: 832px;
    border: 0; border-top: 1.5px solid var(--rule);
  }
  .footer {
    position: absolute; left: 0; right: 0; top: 1160px; padding-left: 22px;
    text-align: center; font-size: 11px; letter-spacing: 0.8px; color: var(--muted);
  }
</style>
</head>
<body>
  <div class="edge-band"></div>

  <aside class="sidebar">
    <div class="brand">
      <span class="brand-name">SkyVane</span>
      <span class="brand-mark"></span>
    </div>
    <div class="brand-tagline">Precision Weather Technologies</div>

    <div class="author">Dale<br>Chief Meteorologist<br>SkyVane</div>
    <hr class="sidebar-rule">
    <div class="issue-date">May 3, 2016</div>

    <p>The summary from the Regional Storm Desk (RSD) from yesterday, tornadoes are Red dots, hail is Green, and winds reports above 58 miles per hour are Blue. The Black squares represent hailstones of 2 inches and larger.</p>
    <p class="highlight">As I said, this is only what was actually reported; most people when they witness severe weather usually do 1 of 2 things: they hide trying to survive, or they record a video and upload it to ClipStream. The result is an under-reporting of severe weather.</p>
    <p>Today will generate the highest threat of severe weather, for tomorrow and Friday, the probability will diminish. Please note that I said “diminish”, not disappear; there is a big difference.</p>
    <p class="highlight">The lengthy frontal zone will get a push of cold air from Canada, and we will see a strong cold front move through most of the Southeast over the weekend. Temperatures will be dropping by 15 to 20 degrees and more in some areas.</p>
  </aside>

  <main class="main">
    <p>We continue to see a frontal boundary that stretches from the East Coast to the West Coast. To the south of the frontal zone, we have hot, humid air, and to the north of the boundary, the airmass is cool and drier.</p>
    <p class="highlight">We will see the formation of another “dry line” over West Texas today, and it will all come together along the Texas – Oklahoma border area. I expect to see more tornadoes, very large hail and wind gusts above 70 miles per hour today.</p>

    <div class="map-frame reports" role="img" aria-label="Map of the United States showing yesterday's severe weather reports: tornado, wind and hail markers"></div>
    <div class="map-caption">RSD Severe Weather Summary for yesterday</div>
    <p>For example, the daytime high temperature in Memphis today will be 83 degrees, but on Sunday it will only reach 60 degrees. Temperatures along the Gulf Coast will remain quite warm throughout the weekend.</p>

    <div class="map-frame outlook" role="img" aria-label="Day 1 categorical severe weather outlook map of the United States with shaded risk areas"></div>
  </main>

  <hr class="footer-rule">
  <div class="footer">SKYVANE - PRECISION WEATHER TECHNOLOGIES</div>
</body>
</html>
```